KORVELTA Corporate Business Card

Modern business card design for company which focuses in the areas of Staffing, IT Consulting & Data Services. Please note: We are no longer using the IT subscript on the logo. All designs should have IT subscript removed.
Website: www.korveltait.example

```html
<!DOCTYPE html>
<html lang="en">
<head>
<meta charset="utf-8">
<title>KORVELTA Business Card</title>
<link href="https://fonts.googleapis.com/css2?family=Lato:wght@400;700&display=swap" rel="stylesheet">
<style>
  :root {
    --backdrop: #3b3b3e;
    --card: #17161b;
    --brand-blue: #1f9be0;
    --text-light: #e9e9ee;
  }
  * { margin: 0; padding: 0; box-sizing: border-box; }
  html, body {
    width: 1200px; height: 1200px; overflow: hidden;
    background: var(--backdrop);
    font-family: "Lato", sans-serif;
  }
  .card {
    position: absolute;
    left: 250px;
    width: 700px; height: 400px;
    background: var(--card);
    border-radius: 90px 0 90px 0;
    box-shadow: 0 12px 30px rgba(0,0,0,.45);
    color: var(--text-light);
  }
  .card--front { top: 170px; }
  .card--back { top: 630px; }

  .wordmark {
    display: flex; align-items: center; gap: 14px;
    color: var(--brand-blue);
    font-weight: 700; letter-spacing: 3px;
  }
  .wordmark__square {
    width: 0.7em; height: 0.7em;
    background: var(--brand-blue);
  }
  .card--front .wordmark {
    position: absolute; left: 50%; top: 50%;
    transform: translate(-50%, -50%);
    font-size: 58px;
  }
  .card--back .wordmark {
    position: absolute; right: 50px; top: 130px;
    font-size: 56px;
  }

  .holder { position: absolute; left: 60px; top: 48px; }
  .holder__name {
    color: var(--brand-blue); font-size: 22px; letter-spacing: 1px;
    text-transform: uppercase;
  }
  .holder__role { font-size: 17px; margin-top: 2px; }

  .contacts {
    position: absolute; left: 40px; bottom: 50px;
    list-style: none; font-size: 19px; line-height: 1.45;
  }
  .contacts li { display: flex; align-items: center; gap: 10px; }
  .contacts svg { width: 15px; height: 15px; fill: var(--brand-blue); flex: none; }

  .address {
    position: absolute; right: 50px; bottom: 40px;
    text-align: right; font-size: 19px; line-height: 1.3; font-style: normal;
  }
</style>
</head>
<body>
  <section class="card card--front">
    <div class="wordmark"><span class="wordmark__square"></span>KORVELTA</div>
  </section>

  <section class="card card--back">
    <div class="holder">
      <p class="holder__name">Daniel Harrow</p>
      <p class="holder__role">Managing Director</p>
    </div>

    <div class="wordmark"><span class="wordmark__square"></span>KORVELTA</div>

    <ul class="contacts">
      <li>
        <svg viewBox="0 0 24 24" aria-hidden="true"><path d="M6.6 10.8a15.1 15.1 0 0 0 6.6 6.6l2.2-2.2a1 1 0 0 1 1-.25 11.4 11.4 0 0 0 3.6.57 1 1 0 0 1 1 1V20a1 1 0 0 1-1 1A17 17 0 0 1 3 4a1 1 0 0 1 1-1h3.5a1 1 0 0 1 1 1c0 1.25.2 2.45.57 3.57a1 1 0 0 1-.25 1z"/></svg>
        555-014-2290
      </li>
      <li>
        <svg viewBox="0 0 24 24" aria-hidden="true"><path d="M2 5h20v14H2z M2 5l10 8 10-8" fill="none" stroke="#1f9be0" stroke-width="2.5"/></svg>
        contactus@korveltait.example
      </li>
      <li>
        <svg viewBox="0 0 24 24" aria-hidden="true"><circle cx="12" cy="12" r="10"/></svg>
        www.korveltait.example
      </li>
    </ul>

    <address class="address">
      48 Ardent Ave<br>
      Westbrook, IN 00000
    </address>
  </section>
</body>
</html>
```